依頼詳細
ラベルのデザインを募集します。

基本的には、幅91.5mm 縦131mmの縦長で角が少し丸いシールにいれるデザインです
・データは様々な形で使用させて頂きます。
(ホームページに載せたり、サンプル品に使用するなど)

クラフトのチャック袋(スタンドパック)にラベルを貼る予定です。
■キャッチフレーズなど
・魔法のスーパーフード タイガーナッツ!パウダータイプ

記載項目
商品名:星屑のコモレビパウダー
その他キャッチフレーズ、キーワードなど:スーパーフード
希望イメージ
シンプル 複雑
単色 カラフル
暗い 明るい
日常 高級
遊び心 厳粛
未来的 伝統的
女性的 男性的
希望する色
赤系、黄・オレンジ系
納品ファイル
• イラストレーター形式 (.ai)
• フォトショップ形式 (.psd)
補足説明
送付ファイルはパウダーの写真です。特に使わなくても大丈夫ですが、色合いなど確認するのにお使いください。
粒状態の画像を追加します。
製品自体は粉なので参考にしてください。
使わなくても大丈夫です。
■ 選んだ理由

自分の考えていたイメージに近く、魔法感がよく出ていて
まとまっていたのでこちらを選ばせて頂きました。

■ 提案者全員のお礼・コメント

多数のご応募ありがとうございました。
またの機会がありましたら、よろしくお願い足します。

```html
<!DOCTYPE html>
<html lang="ja">
<head>
<meta charset="utf-8">
<title>星屑のコモレビパウダー ラベル</title>
<link rel="stylesheet" href="https://fonts.googleapis.com/css2?family=Oswald:wght@500;600&family=M+PLUS+Rounded+1c:wght@500;700;800&family=Yusei+Magic&display=swap">
<style>
  :root {
    --paper: #ffffff;
    --ink: #2b2420;
    --red: #c8231e;
    --red-deep: #a11a16;
    --gold: #f5d23c;
    --bubble: #f3ede4;
    --vit: #e9b21f;
    --mineral: #e9872a;
    --oleic: #9b6fb3;
    --fiber: #7fa94a;
    --nut-light: #c9a67a;
    --nut-dark: #6b4a2d;
    --powder: #e6d7bf;
  }
  * { margin: 0; padding: 0; box-sizing: border-box; }
  html, body { width: 863px; height: 1200px; overflow: hidden; background: var(--paper); }
  .label {
    position: relative; width: 863px; height: 1200px; overflow: hidden;
    background: var(--paper); border-radius: 36px;
    font-family: "M PLUS Rounded 1c", sans-serif; color: var(--ink);
  }
  .nuts-photo {
    position: absolute; left: 0; top: 560px; width: 863px; height: 640px;
    background: radial-gradient(ellipse at 60% 40%, var(--nut-light) 0%, #a47a4f 45%, var(--nut-dark) 100%);
  }
  .ribbon {
    position: absolute; left: 161px; top: 34px; width: 540px; height: 96px;
  }
  .ribbon svg { position: absolute; inset: 0; width: 100%; height: 100%; }
  .ribbon-text {
    position: absolute; left: 44px; top: 6px; width: 452px; height: 84px;
    display: flex; align-items: center; justify-content: center; white-space: nowrap;
    font-family: "Oswald", sans-serif; font-weight: 600; font-size: 54px; letter-spacing: 2px; color: var(--gold);
  }
  .kana-sub { position: absolute; top: 136px; width: 100%; text-align: center; font-weight: 700; font-size: 34px; color: var(--ink); }
  .title-en {
    position: absolute; top: 192px; width: 100%; text-align: center; white-space: nowrap;
    font-family: "Oswald", sans-serif; font-weight: 500; font-size: 100px; line-height: 1.1; letter-spacing: 1px; color: var(--ink);
  }
  .title-ja {
    position: absolute; top: 318px; width: 100%; text-align: center; white-space: nowrap;
    font-family: "Yusei Magic", sans-serif; font-size: 66px; line-height: 1.2; color: var(--red); letter-spacing: 2px;
  }
  .powder-photo {
    position: absolute; left: 405px; top: 445px; width: 210px; height: 210px; border-radius: 50%;
    background: radial-gradient(circle at 45% 40%, #f1e6d3 0%, var(--powder) 55%, #cbb393 100%);
    border: 6px solid var(--paper); z-index: 2;
  }
  .bubble {
    position: absolute; width: 170px; height: 170px; border-radius: 50%; background: var(--bubble);
    display: flex; align-items: center; justify-content: center; text-align: center;
    font-weight: 800; font-size: 26px; line-height: 1.3; color: var(--red-deep); z-index: 1;
  }
  .bubble.nutrition { left: 250px; top: 445px; }
  .bubble.powder-type { left: 640px; top: 455px; }
  .nutrient {
    position: absolute; width: 150px; height: 150px; border-radius: 50%;
    display: flex; align-items: center; justify-content: center; text-align: center; white-space: nowrap;
    font-weight: 800; font-size: 24px; line-height: 1.2; color: #fff; border: 5px solid var(--paper); z-index: 3;
  }
  .nutrient.vitamin { left: 40px; top: 600px; background: var(--vit); }
  .nutrient.mineral { left: 200px; top: 600px; background: var(--mineral); }
  .nutrient.oleic { left: 40px; top: 760px; background: var(--oleic); }
  .nutrient.fiber { left: 200px; top: 760px; background: var(--fiber); }
  .maker {
    position: absolute; right: 40px; bottom: 34px; font-weight: 700; font-size: 20px;
    letter-spacing: 1px; color: var(--paper);
  }
</style>
</head>
<body>
  <main class="label">
    <div class="nuts-photo" role="img" aria-label="皿に盛られたタイガーナッツの粒の写真"></div>

    <div class="ribbon">
      <svg viewBox="0 0 540 96" aria-hidden="true">
        <polygon points="0,18 60,18 60,84 0,84 24,51" fill="var(--red-deep)"/>
        <polygon points="540,18 480,18 480,84 540,84 516,51" fill="var(--red-deep)"/>
        <rect x="44" y="6" width="452" height="84" fill="var(--red)"/>
      </svg>
      <span class="ribbon-text">SUPER FOOD</span>
    </div>
    <p class="kana-sub">スーパーフード</p>

    <h1 class="title-en">TIGER NUTS POWDER</h1>
    <p class="title-ja">星屑のコモレビパウダー</p>

    <div class="bubble nutrition">栄養豊富<br>なのに<br>低カロリー</div>
    <div class="powder-photo" role="img" aria-label="タイガーナッツパウダーの粉の写真"></div>
    <div class="bubble powder-type">便利な<br>パウダー<br>タイプ!</div>

    <div class="nutrient vitamin">ビタミンE</div>
    <div class="nutrient mineral">ミネラル</div>
    <div class="nutrient oleic">オレイン酸</div>
    <div class="nutrient fiber">食物繊維</div>

    <p class="maker">HOSHIKUZU FOODS</p>
  </main>
</body>
</html>
```